Postcard for Antique Furniture Restorer

My business is to restore antique furniture. I am based in Sydney, Australia.

I will be using this postcard to promote my business.
I will give it to customers like a With Compliments card.

Sometimes I will be writing information on the back of the card.

Design for Postcard Size eg 148 X 105mm

Front of card:

Attached are images of Antique furniture - please use ONLY 1 of the 3 images.
Deep etch the image on a white or cream background.

On front of card add these words:
Timber Awakened
antique furniture restoration

Antiques travel through time, seeing generations of families
Through time they remain - they tell a continuing story
Be part of the journey

Back of postcard:
(leave space for notes to be handwritten)

Add these words:

Timber Awakened
Corwin Aldace
mobile 0437 552 681
www.oakmendworks.com.au

Industry/Entity Type

Business

Font styles to use
Serif
Sans Serif

Colors
fefdec
ffffff

Requirements
Must have
• Use only 1 image. Image must be deep etched.

```html
<!DOCTYPE html>
<html lang="en">
<head>
<meta charset="utf-8">
<title>Timber Awakened – Postcard</title>
<link href="https://fonts.googleapis.com/css2?family=Rye&family=Cardo&family=Tenor+Sans&display=swap" rel="stylesheet">
<style>
  :root {
    --brown: #6a3b12;
    --brown-soft: #7a4a1e;
    --border-gold: #a9834f;
    --border-dark: #6e4c28;
    --card: #ffffff;
    --wood-dark: #4a2412;
    --wood-mid: #8a3f18;
    --wood-light: #b5652a;
  }
  * { margin: 0; padding: 0; box-sizing: border-box; }
  html, body { width: 1200px; height: 863px; overflow: hidden; background: #fff; }
  .postcard {
    position: relative;
    width: 1200px; height: 863px;
    overflow: hidden;
  }
  .pattern-border {
    position: absolute; inset: 0;
    background: radial-gradient(circle at 50% 50%, var(--border-gold), var(--border-dark));
  }
  .card-panel {
    position: absolute;
    left: 22px; top: 14px; width: 1158px; height: 834px;
    background: var(--card);
    clip-path: polygon(0.6% 1.2%, 12% 0.4%, 30% 1.1%, 52% 0.2%, 74% 1%, 92% 0.3%, 99.4% 1.4%,
      100% 20%, 99.2% 45%, 100% 70%, 99.4% 98.6%, 80% 99.6%, 55% 98.9%, 30% 99.8%, 8% 99%, 0.5% 99.6%,
      0% 75%, 0.8% 50%, 0% 25%);
  }
  .rule {
    position: absolute; top: 136px; height: 2px; background: var(--brown);
  }
  .rule--left { left: 75px; width: 455px; }
  .rule--right { left: 610px; width: 455px; }
  .flourish {
    position: absolute; left: 470px; top: 30px; width: 260px; height: 165px;
    background: radial-gradient(ellipse at center, rgba(122,74,30,0.28), rgba(122,74,30,0) 70%);
  }
  .brand-name {
    position: absolute; left: 64px; top: 198px;
    font-family: "Rye", serif;
    font-size: 62px; line-height: 68px;
    letter-spacing: 2px;
    color: var(--brown);
    text-transform: uppercase;
    font-weight: 400;
  }
  .tagline {
    position: absolute; left: 66px; top: 342px;
    font-family: "Cardo", serif;
    font-size: 38px;
    color: var(--brown);
  }
  .story {
    position: absolute; left: 66px; top: 533px;
    font-family: "Tenor Sans", sans-serif;
    font-size: 27px; line-height: 39px;
    color: var(--brown-soft);
  }
  .story p { margin-bottom: 42px; }
  .story .indent { padding-left: 44px; }
  .armoire {
    position: absolute; left: 725px; top: 180px; width: 380px; height: 545px;
    background: linear-gradient(135deg, var(--wood-dark), var(--wood-mid) 45%, var(--wood-light) 70%, var(--wood-dark));
    clip-path: polygon(2% 3%, 100% 0%, 98% 6%, 92% 8%, 92% 86%, 86% 100%, 82% 89%, 10% 84%, 6% 84%, 3% 86%, 5% 78%, 5% 7%);
  }
</style>
</head>
<body>
<div class="postcard">
  <div class="pattern-border" role="img" aria-label="Ornate brocade pattern framing the card"></div>
  <div class="card-panel"></div>

  <div class="rule rule--left"></div>
  <div class="rule rule--right"></div>
  <div class="flourish" role="img" aria-label="Decorative scroll flourish"></div>

  <h1 class="brand-name">Timber<br>Awakened</h1>
  <p class="tagline">antique furniture restoration</p>

  <div class="story">
    <p>Antiques travel through time,<br><span class="indent">seeing generations of families</span></p>
    <p>Through time they remain~they tell a continuing story</p>
    <p>Be part of the journey…</p>
  </div>

  <div class="armoire" role="img" aria-label="Deep-etched photograph of a carved burl walnut antique armoire with two doors"></div>
</div>
</body>
</html>
```